Business Card Design

I am a new realtor. To stand out from the other 25 realtors in my firm I need a card that will stand out. I am the youngest realtor here, so I want something to reflect that. Something different, as opposed to the same old traditional, boring cards everyone else has. It of course needs to have my picture which I will download for you ( I included a black and white option as well as color. Either are fine) and you can crop it or do whatever you need to make it look the best. Our company colors are red and white. These don't have to be the only colors on the card, but the red especially needs to be a focal color. I like a clean, stream-line look while still eye-catching. Not over the top busy.
While I do have to provide the company logo, I am a contractor. Therefore, I want the focus on me and my information.
Industry/Entity Type
Realtor
Contact Information for Business Card
Marisa Quillon
Realtor (this needs the realtor logo which has the R in the circle at the end)
(office)555.318.4406
(cell) 555.892.6035
Mquillon@brv-homegroup.example
It will also need our company logo which I will download and send
Requirements
Nice to have
- I like the look of the foil or metallic. However, this is definitely not a requirement

```html
<!DOCTYPE html>
<html lang="en">
<head>
<meta charset="utf-8">
<title>Marisa Quillon — Business Card</title>
<link rel="stylesheet" href="https://fonts.googleapis.com/css2?family=Arimo:wght@400&family=Crimson+Text:ital@1&family=Tinos:wght@400&display=swap">
<style>
  :root {
    --backdrop: #e4e5e7;
    --brand-red: #d8191c;
    --brand-red-dark: #b81316;
    --card-white: #ffffff;
    --ink: #1d1d1d;
    --rule: #9a9a9a;
    --photo-light: #eeeae6;
    --photo-mid: #b39682;
    --photo-dark: #6b4a36;
  }
  * { box-sizing: border-box; margin: 0; padding: 0; }
  html, body {
    width: 1200px; height: 800px; overflow: hidden;
    background: var(--backdrop);
  }
  .canvas {
    position: relative; width: 1200px; height: 800px;
    display: flex; align-items: center; justify-content: center; gap: 60px;
  }
  .card {
    position: relative; width: 520px; height: 297px; overflow: hidden;
    box-shadow: 0 10px 24px rgba(0,0,0,0.14);
  }

  /* Front: brokerage side */
  .card--front {
    background: var(--brand-red);
    display: flex; align-items: center; justify-content: center;
  }
  .brokerage-name {
    font-family: "Tinos", serif; font-weight: 400;
    color: var(--card-white); text-align: center; line-height: 1.15;
  }
  .brokerage-name__main { font-size: 32px; letter-spacing: 1px; text-transform: uppercase; }
  .brokerage-name__sub { font-size: 22px; margin-top: 6px; }

  /* Back: agent side */
  .card--agent { background: var(--card-white); }
  .agent-name {
    position: absolute; left: 170px; top: 34px;
    font-family: "Crimson Text", serif; font-style: italic;
    font-size: 32px; color: var(--ink);
  }
  .agent-name .initial { color: var(--brand-red); }
  .agent-rule {
    position: absolute; left: 150px; top: 82px; width: 270px; height: 1px;
    background: linear-gradient(90deg, var(--rule), #cfcfcf);
  }
  .agent-title {
    position: absolute; left: 320px; top: 90px;
    font-family: "Arimo", sans-serif; font-size: 16px; color: var(--ink);
  }
  .contact-list {
    position: absolute; left: 92px; top: 104px; list-style: none;
    font-family: "Arimo", sans-serif; font-size: 12.5px; color: var(--ink);
  }
  .contact-list li { display: flex; gap: 12px; line-height: 20px; }
  .contact-list .label { color: var(--brand-red); font-weight: 700; width: 10px; }
  .accent-band {
    position: absolute; left: 0; bottom: 0; width: 330px; height: 30px;
    background: var(--brand-red);
  }
  .accent-band::after {
    content: ""; position: absolute; left: 0; top: 0; width: 100%; height: 4px;
    background: var(--brand-red-dark);
  }
  .agent-photo {
    position: absolute; left: 330px; top: 118px; width: 180px; height: 179px;
    background:
      radial-gradient(ellipse 40% 45% at 55% 35%, var(--photo-mid), transparent 70%),
      radial-gradient(ellipse 55% 60% at 55% 40%, var(--photo-dark) 0%, transparent 75%),
      linear-gradient(180deg, var(--card-white) 0%, var(--photo-light) 100%);
  }
</style>
</head>
<body>
  <main class="canvas">
    <section class="card card--front" aria-label="Card front">
      <div class="brokerage-name">
        <div class="brokerage-name__main">Delphine Marsh<br>&amp; Company</div>
        <div class="brokerage-name__sub">Real Estate Brokerage</div>
      </div>
    </section>

    <section class="card card--agent" aria-label="Card back">
      <h1 class="agent-name"><span class="initial">M</span>arisa <span class="initial">Q</span>uillon</h1>
      <div class="agent-rule"></div>
      <p class="agent-title">Realtor ®</p>
      <ul class="contact-list">
        <li><span class="label">P</span><span>555.318.4406</span></li>
        <li><span class="label">C</span><span>555.892.6035</span></li>
        <li><span class="label">E</span><span>Mquillon@brv-homegroup.example</span></li>
      </ul>
      <div class="accent-band"></div>
      <div class="agent-photo" role="img" aria-label="Portrait photo of the realtor in a white blouse and beaded necklace"></div>
    </section>
  </main>
</body>
</html>
```